Software company specialized in data analytics and professional services

We need a landing page design for our business. It should include our logo design. It should have multiple sections :
- stylish head
- what we do (data analytics software, professional services)
- contact form

Target Market(s)

Companies, B2B

Industry/Entity Type

Data

Number of Pages Required

1 page

Font styles to use
Sans Serif

Requirements
Must have
• Dark theme
Should not have
• Gradients on buttons

```html
<!DOCTYPE html>
<html lang="en">
<head>
<meta charset="utf-8">
<title>Northgrid — Data Analysis Company</title>
<link href="https://fonts.googleapis.com/css2?family=Poppins:wght@400;500;600;800&display=swap" rel="stylesheet">
<style>
:root{
  --magenta:#e10098;
  --purple:#9a00e6;
  --bg:#15112f;
  --navy:#1e1548;
  --footer:#0d0a22;
  --ink:#ffffff;
  --muted:#aaa6c6;
  --card:#221b4d;
  --panel:#1c1640;
  --field:#15112f;
  --white:#ffffff;
  --dark-text:#111111;
  --grad:linear-gradient(90deg,var(--magenta),var(--purple));
}
*{box-sizing:border-box;margin:0;padding:0}
html,body{width:1200px;height:3943px;overflow:hidden}
body{font-family:'Poppins',sans-serif;color:var(--ink);background:var(--bg);position:relative}
.abs{position:absolute}
.btn{position:absolute;display:flex;align-items:center;justify-content:center;border-radius:16px;font-size:15px;font-weight:500;text-transform:uppercase;letter-spacing:.2px;white-space:nowrap}
.btn-solid{background:var(--magenta);color:var(--white)}
.btn-light{background:var(--white);color:var(--dark-text)}
.eyebrow{font-size:15px;font-weight:500;text-transform:uppercase;position:absolute}
.eyebrow::after{content:"";display:block;width:72px;height:2px;background:var(--magenta);margin:4px auto 0}
.eyebrow.left::after{margin-left:0}
.h2{font-weight:800;font-size:44px;line-height:1.2;position:absolute}
.center{left:0;width:1200px;text-align:center}

/* top bar */
.topbar{top:0;left:0;width:1200px;height:34px;background:var(--grad);color:var(--white);font-size:15px}
.topbar span{position:absolute;top:7px;display:flex;align-items:center;gap:10px}
/* header */
.header{top:34px;left:0;width:1200px;height:76px;background:var(--navy)}
.brand{position:absolute;left:12px;top:16px;font-size:38px;font-weight:600;color:var(--magenta);letter-spacing:1px;line-height:44px}
.nav{position:absolute;left:378px;top:30px;display:flex;gap:32px;font-size:14px;font-weight:500;color:var(--white)}
.header .btn{left:1018px;top:26px;width:138px;height:32px}
/* hero */
.hero{top:110px;left:0;width:1200px;height:588px;background:linear-gradient(110deg,#2a2b30,#4e473f 45%,#1f2126)}
.hero h1{position:absolute;top:135px;left:0;width:1200px;text-align:center;color:var(--white);font-weight:800;font-size:58px;line-height:68px}
.hero p{position:absolute;top:284px;left:0;width:1200px;text-align:center;color:var(--white);font-size:15px;line-height:24px}
.hero .btn{left:513px;top:390px;width:138px;height:30px}
.dots{position:absolute;top:543px;left:509px;display:flex;gap:26px}
.dots i{width:22px;height:22px;border-radius:50%;background:var(--white);display:block}
.dots i.ring{background:none;border:3px solid var(--white)}
/* about */
.about-frame{top:770px;left:128px;width:409px;height:372px;border-radius:20px;background:linear-gradient(180deg,var(--magenta),var(--purple))}
.about-gap{top:908px;left:128px;width:409px;height:96px;background:var(--bg)}
.about-photo{top:802px;left:156px;width:352px;height:307px;border-radius:14px;background:linear-gradient(135deg,#d9d3cc,#4a4e57 60%,#2b2f36)}
.about-text{left:620px;top:790px;width:500px}
.about-text .eyebrow{position:static}
.about-text h2{font-weight:800;font-size:44px;line-height:53px;margin-top:14px}
.about-text p{font-size:11px;line-height:20px;color:var(--muted);margin-top:22px}
.about .btn{left:620px;top:1057px;width:138px;height:30px}
/* banner */
.banner{top:1208px;left:0;width:1200px;height:200px;background:var(--grad)}
.banner h2{position:absolute;left:136px;top:42px;color:var(--white);font-weight:800;font-size:44px;line-height:53px}
.banner .btn{left:920px;top:85px;width:138px;height:30px}
/* services */
.svc-card{position:absolute;top:1627px;width:219px;height:263px;background:var(--card)}
.svc-card svg{position:absolute;left:30px;top:42px}
.svc-card h3{position:absolute;left:34px;top:118px;font-size:22px;font-weight:500;line-height:26px}
.plus{position:absolute;top:243px;width:36px;height:36px;background:var(--magenta);color:var(--white);display:flex;align-items:center;justify-content:center;font-size:30px;font-weight:600}
/* professional */
.pro{top:1993px;left:0;width:1200px;height:404px;background:linear-gradient(110deg,#231a5a,#2b2470 45%,#0c6e93)}
.pro h2{position:absolute;top:70px;left:0;width:1200px;text-align:center;color:var(--white);font-weight:800;font-size:44px}
.pro p{position:absolute;top:136px;left:0;width:1200px;text-align:center;color:var(--white);font-size:12px;line-height:20px}
.pro .btn{left:526px;top:236px;width:138px;height:30px}
.tabs{position:absolute;top:338px;left:228px}
.tab-label{position:absolute;top:20px;font-size:19px;font-weight:600;white-space:nowrap;line-height:26px}
/* testimonials */
.tcard{position:absolute;top:2625px;width:475px;height:228px;background:var(--card);overflow:hidden}
.tcard svg.deco{position:absolute;left:0;top:0}
.avatar{position:absolute;left:40px;top:50px;width:110px;height:110px;border-radius:50%;background:linear-gradient(135deg,#c9ccd1,#5a6f8a);border:4px solid var(--white)}
.tcard h4{position:absolute;left:170px;top:50px;font-size:21px;font-weight:500}
.stars{position:absolute;left:170px;top:82px;color:#d4ae55;font-size:22px;letter-spacing:3px}
.tcard p{position:absolute;left:170px;top:122px;width:270px;font-size:10.5px;line-height:18px;color:var(--muted)}
/* contact */
.c-bar-top{top:2943px;left:86px;width:407px;height:80px;border-radius:22px 22px 0 0;background:var(--grad)}
.c-bar-bot{top:3384px;left:86px;width:407px;height:80px;border-radius:0 0 22px 22px;background:var(--grad)}
.c-photo{top:2988px;left:0;width:579px;height:419px;background:linear-gradient(135deg,#8b5a3c,#c9b9a6 50%,#5a4a44)}
.c-panel{top:2988px;left:579px;width:621px;height:419px;background:var(--panel)}
.field{position:absolute;border:1px solid #c25fb5;background:var(--field);font-size:16px;color:var(--muted);padding:12px 16px}
/* footer */
.footer{top:3566px;left:0;width:1200px;height:377px;background:var(--footer);color:var(--white)}
.f-brand{position:absolute;left:116px;top:90px;font-size:34px;font-weight:600;display:flex;align-items:center;gap:12px}
.f-brand i{width:22px;height:22px;border-radius:50%;background:var(--magenta);display:block}
.footer p.about{position:absolute;left:116px;top:184px;width:270px;font-size:11px;line-height:18px;color:var(--muted)}
.f-title{position:absolute;top:86px;font-size:21px;font-weight:500}
.f-list{position:absolute;left:550px;top:124px;list-style:none;font-size:15px}
.f-list li{display:flex;align-items:center;gap:12px;height:35px}
.f-list li::before{content:"";width:12px;height:12px;border-radius:50%;background:var(--magenta)}
.f-contact{position:absolute;left:866px;top:128px;font-size:15px}
.f-contact div{display:flex;align-items:center;gap:14px;height:48px}
.copy{position:absolute;left:122px;top:314px;font-size:11px}
.social{position:absolute;top:310px;width:28px;height:28px;border-radius:50%;background:var(--magenta)}
</style>
</head>
<body>

<div class="abs topbar">
  <span style="left:20px">
    <svg width="18" height="18" viewBox="0 0 24 24"><path fill="#fff" d="M6.6 10.8a15 15 0 0 0 6.6 6.6l2.2-2.2c.3-.3.7-.4 1-.2 1.1.4 2.3.6 3.6.6.6 0 1 .4 1 1V20c0 .6-.4 1-1 1A17 17 0 0 1 3 4c0-.6.4-1 1-1h3.5c.6 0 1 .4 1 1 0 1.3.2 2.5.6 3.6.1.3 0 .7-.2 1z"/></svg>
    (+62)555 010 274</span>
  <span style="left:262px">
    <svg width="20" height="16" viewBox="0 0 20 16"><rect x="1" y="2" width="18" height="13" rx="1" fill="#fff"/><path d="M1 3l9 6 9-6" stroke="#b01ac0" stroke-width="1.6" fill="none"/></svg>
    hello@northgrid.example</span>
</div>

<header class="abs header">
  <div class="brand">NORTHGRID</div>
  <nav class="nav"><span>HOME</span><span>ABOUT</span><span>SERVICES</span><span>WHY CHOOSE US</span><span>TESTIMONIALS</span></nav>
  <div class="btn btn-solid">Contact Us</div>
</header>

<section class="abs hero" role="img" aria-label="Photo of two colleagues working together at a laptop in a bright office">
  <h1>Best Data<br>Analysis Company</h1>
  <p>Lorem ipsum dolor sit amet, consectetur adipiscing elit,<br>sed do eiusmod tempor incididunt ut labore<br>et dolore magna aliqua.</p>
  <div class="btn btn-solid">Contact Us</div>
  <div class="dots"><i></i><i class="ring"></i><i></i></div>
</section>

<section class="about">
  <div class="abs about-frame"></div>
  <div class="abs about-gap"></div>
  <div class="abs about-photo" role="img" aria-label="Photo of an analyst reviewing dashboards on a laptop"></div>
  <div class="abs about-text">
    <div class="eyebrow left">About Us</div>
    <h2>Best Data<br>Analysis Company</h2>
    <p>Lorem ipsum dolor sit amet, consectetur adipiscing elit, sed do eiusmod tempor incididunt ut labore et dolore magna aliqua. Ut enim ad minim veniam, quis nostrud exercitation ullamco laboris nisi ut aliquip ex ea commodo consequat. Duis aute irure dolor in reprehenderit in voluptate velit esse cillum dolore eu fugiat nulla pariatur.</p>
  </div>
  <div class="btn btn-solid">Read More</div>
</section>

<section class="abs banner">
  <h2>Hundreds of Customers<br>Trust Our Digital Agency</h2>
  <div class="btn btn-light">Read More</div>
</section>

<section class="services">
  <div class="eyebrow center" style="top:1472px">What We Do</div>
  <h2 class="h2 center" style="top:1506px">Our Professional Services</h2>

  <div class="svc-card" style="left:121px">
    <svg width="66" height="66" viewBox="0 0 66 66" fill="none" stroke="#ff2fb4" stroke-width="2.2"><rect x="2" y="2" width="54" height="44" rx="3"/><line x1="2" y1="11" x2="56" y2="11"/><circle cx="38" cy="38" r="14"/><line x1="48" y1="48" x2="62" y2="62" stroke-width="4"/><path d="M31 44V36M36 44V31M41 44V34M46 44V38"/></svg>
    <h3>Data<br>Analysis</h3><div class="plus" style="left:46px">+</div>
  </div>
  <div class="svc-card" style="left:363px">
    <svg width="66" height="66" viewBox="0 0 66 66" fill="none" stroke="#ff2fb4" stroke-width="2.2"><rect x="4" y="2" width="44" height="60" rx="3"/><circle cx="18" cy="16" r="7"/><line x1="30" y1="12" x2="42" y2="12"/><line x1="30" y1="19" x2="42" y2="19"/><line x1="10" y1="30" x2="42" y2="30"/><path d="M14 54V46M22 54V40M30 54V44M38 54V36"/></svg>
    <h3>Reporting<br>Automation</h3><div class="plus" style="left:48px">+</div>
  </div>
  <div class="svc-card" style="left:606px">
    <svg width="70" height="66" viewBox="0 0 70 66" fill="none" stroke="#ff2fb4" stroke-width="2.2"><rect x="4" y="2" width="62" height="48" rx="3"/><line x1="4" y1="11" x2="66" y2="11"/><rect x="12" y="18" width="12" height="10"/><rect x="29" y="18" width="12" height="10"/><rect x="46" y="18" width="12" height="10"/><circle cx="16" cy="52" r="8"/><circle cx="16" cy="52" r="3"/></svg>
    <h3>Data<br>Management</h3><div class="plus" style="left:52px">+</div>
  </div>
  <div class="svc-card" style="left:848px">
    <svg width="66" height="66" viewBox="0 0 66 66" fill="none" stroke="#ff2fb4" stroke-width="2.2"><rect x="2" y="2" width="40" height="56" rx="3"/><text x="8" y="16" font-size="13" fill="#ff2fb4" stroke="none" font-family="Poppins,sans-serif">$</text><line x1="8" y1="26" x2="30" y2="26"/><line x1="8" y1="34" x2="26" y2="34"/><circle cx="40" cy="38" r="16"/><path d="M32 44l6-6 4 4 8-10"/></svg>
    <h3>Financial<br>Analytics</h3><div class="plus" style="left:56px">+</div>
  </div>
</section>

<section class="abs pro" role="img" aria-label="Dark blue background with a softly faded photo of a team meeting">
  <h2>Professional Services</h2>
  <p>Lorem ipsum dolor sit amet, consectetur adipiscing elit, sed do eiusmod tempor<br>incididunt ut labore et dolore magna aliqua. Ut enim ad minim veniam, quis nostrud<br>exercitation ullamco laboris nisi ut aliquip ex ea commodo consequat. Duis aute irure<br>dolor in reprehenderit in voluptate velit esse cillum dolore eu fugiat nulla pariatur.</p>
  <div class="btn btn-light">Read More</div>
  <div class="tabs">
    <svg width="752" height="66" viewBox="0 0 752 66" style="position:absolute;left:0;top:0">
      <polygon points="0,0 250,0 272,33 250,66 0,66" fill="#e10098"/>
      <polygon points="250,0 500,0 522,33 500,66 250,66 272,33" fill="#ffffff"/>
      <polygon points="500,0 730,0 752,33 730,66 500,66 522,33" fill="#c409b8"/>
    </svg>
    <span class="tab-label" style="left:30px;color:#fff">Business Growth</span>
    <span class="tab-label" style="left:289px;color:#111">Professional Services</span>
    <span class="tab-label" style="left:555px;color:#fff">Financial Advice</span>
  </div>
</section>

<section class="testimonials">
  <div class="eyebrow center" style="top:2477px">Testimonials</div>
  <h2 class="h2 center" style="top:2512px">What Client Say’s</h2>

  <div class="tcard" style="left:92px">
    <svg class="deco" width="190" height="228" viewBox="0 0 190 228"><defs><linearGradient id="tg1" x1="0" x2="1"><stop offset="0" stop-color="#e10098"/><stop offset="1" stop-color="#9a00e6"/></linearGradient></defs><polygon points="0,0 135,0 0,228" fill="#3a2f86"/><polygon points="28,228 90,120 190,228" fill="url(#tg1)"/></svg>
    <div class="avatar" role="img" aria-label="Client portrait"></div>
    <h4>Daniel Reyes</h4><div class="stars">★★★★★</div>
    <p>Lorem ipsum dolor sit amet, consectetur adipiscing elit, sed do eiusmod tempor incididunt ut labore et dolore magna aliqua. et enim ad minim veniam, quis nostrud</p>
  </div>
  <div class="tcard" style="left:629px">
    <svg class="deco" width="190" height="228" viewBox="0 0 190 228"><defs><linearGradient id="tg2" x1="0" x2="1"><stop offset="0" stop-color="#e10098"/><stop offset="1" stop-color="#9a00e6"/></linearGradient></defs><polygon points="0,0 135,0 0,228" fill="#3a2f86"/><polygon points="28,228 90,120 190,228" fill="url(#tg2)"/></svg>
    <div class="avatar" role="img" aria-label="Client portrait"></div>
    <h4>Daniel Reyes</h4><div class="stars">★★★★★</div>
    <p>Lorem ipsum dolor sit amet, consectetur adipiscing elit, sed do eiusmod tempor incididunt ut labore et dolore magna aliqua. et enim ad minim veniam, quis nostrud</p>
  </div>
</section>

<section class="contact">
  <div class="abs c-bar-top"></div>
  <div class="abs c-bar-bot"></div>
  <div class="abs c-photo" role="img" aria-label="Photo of smiling coworkers gathered around a laptop"></div>
  <div class="abs c-panel"></div>
  <div class="eyebrow left" style="left:633px;top:3033px">Have Any Question</div>
  <h2 class="h2" style="left:636px;top:3066px;font-size:42px">CONTACT US</h2>
  <div class="field" style="left:644px;top:3139px;width:239px;height:46px">Name</div>
  <div class="field" style="left:909px;top:3139px;width:239px;height:46px">Email</div>
  <div class="field" style="left:644px;top:3197px;width:239px;height:46px">Phone</div>
  <div class="field" style="left:909px;top:3197px;width:239px;height:46px">Subject</div>
  <div class="field" style="left:644px;top:3257px;width:504px;height:92px">Message</div>
</section>

<footer class="abs footer">
  <div class="f-brand"><i></i>NORTHGRID</div>
  <p class="about">Lorem ipsum dolor sit amet, consectetur adipiscing elit, sed do eiusmod tempor incididunt ut labore et dolore magna aliqua. et enim ad minim veniam, quis nostrud</p>
  <div class="f-title" style="left:550px">EXPLORE</div>
  <ul class="f-list"><li>Home</li><li>About</li><li>Services</li><li>Contact</li></ul>
  <div class="f-title" style="left:866px">CONTACT</div>
  <div class="f-contact">
    <div><svg width="20" height="20" viewBox="0 0 24 24"><path fill="#e10098" d="M6.6 10.8a15 15 0 0 0 6.6 6.6l2.2-2.2c.3-.3.7-.4 1-.2 1.1.4 2.3.6 3.6.6.6 0 1 .4 1 1V20c0 .6-.4 1-1 1A17 17 0 0 1 3 4c0-.6.4-1 1-1h3.5c.6 0 1 .4 1 1 0 1.3.2 2.5.6 3.6.1.3 0 .7-.2 1z"/></svg>(+62)555 010 274</div>
    <div><svg width="22" height="18" viewBox="0 0 20 16"><rect x="1" y="2" width="18" height="13" rx="1" fill="#e10098"/><path d="M1 3l9 6 9-6" stroke="#0d0a22" stroke-width="1.6" fill="none"/></svg>hello@northgrid.example</div>
    <div><svg width="20" height="22" viewBox="0 0 24 24"><path fill="#e10098" d="M12 2a7 7 0 0 0-7 7c0 5 7 13 7 13s7-8 7-13a7 7 0 0 0-7-7zm0 9.5A2.5 2.5 0 1 1 12 6.5a2.5 2.5 0 0 1 0 5z"/></svg>Jl. Melati No.12, Sanur</div>
  </div>
  <div class="copy">Copyright 2023, All Rights Reserved</div>
  <span class="social" style="left:963px"></span>
  <span class="social" style="left:1008px"></span>
  <span class="social" style="left:1053px"></span>
</footer>

</body>
</html>
```